Stationery & Envelope Design

Executive Style looking stationery & envelope design.
Business Information:
Harrow Crest Realty
7385 Brindle Hollow Lane, Roseville, CA 95661-2049
Phone: 916.555.0142
Fax: 916.555.0187

Industry/Entity Type

Business

```html
<!DOCTYPE html>
<html lang="en">
<head>
<meta charset="utf-8">
<title>Harrow Crest Realty — Letterhead</title>
<link rel="stylesheet" href="https://fonts.googleapis.com/css2?family=Questrial&display=swap">
<style>
  :root {
    --paper: #ffffff;
    --navy: #2b3256;
    --gold: #e9cf4a;
    --olive: #6f7d3e;
    --ink: #2a2a2a;
  }
  * { margin: 0; padding: 0; box-sizing: border-box; }
  html, body {
    width: 849px;
    height: 1200px;
    overflow: hidden;
    background: var(--paper);
  }
  .letterhead {
    position: relative;
    width: 849px;
    height: 1200px;
    background: var(--paper);
    font-family: "Questrial", sans-serif;
  }
  .brand {
    position: absolute;
    left: 20px;
    top: 93px;
    display: flex;
    align-items: center;
    gap: 10px;
  }
  .brand-mark {
    width: 16px;
    height: 16px;
    background: var(--olive);
  }
  .brand-name {
    font-size: 22px;
    letter-spacing: 0.4px;
    text-transform: uppercase;
    color: var(--navy);
    line-height: 1;
    white-space: nowrap;
  }
  .side-band {
    position: absolute;
    left: 801px;
    top: 349px;
    width: 43px;
    height: 851px;
  }
  .sender {
    position: absolute;
    left: 33px;
    top: 1072px;
    font-variant: small-caps;
    font-size: 15px;
    line-height: 20.5px;
    letter-spacing: 2px;
    color: var(--ink);
    font-style: normal;
  }
</style>
</head>
<body>
  <main class="letterhead">
    <header class="brand">
      <span class="brand-mark"></span>
      <span class="brand-name">Harrow Crest Realty</span>
    </header>

    <svg class="side-band" viewBox="0 0 43 851" aria-hidden="true">
      <rect x="0" y="0" width="43" height="851" fill="var(--navy)"/>
      <rect x="0" y="0" width="43" height="19" fill="var(--gold)"/>
      <rect x="0" y="26" width="43" height="13" fill="var(--gold)"/>
      <rect x="0" y="47" width="43" height="9" fill="var(--gold)"/>
      <rect x="0" y="68" width="43" height="5" fill="var(--olive)"/>
      <rect x="0" y="103" width="43" height="7" fill="var(--olive)"/>
    </svg>

    <address class="sender">
      Harrow Crest Realty<br>
      7385 Brindle Hollow Lane<br>
      Linden Falls,&nbsp; CA 95661-2049<br>
      Phone: 916.555.0142<br>
      Fax: 916.555.0187
    </address>
  </main>
</body>
</html>
```